Letterhead PT. Kencana Tirta Mandiri Developer

Alo , My Company need a letterhead design for PT. Kencana Tirta Mandiri developer Real Estate , i need your each other creative design letterhead for my PT.Kencana Tirta Mandiri Developer Real Estate guys
input my data in letterhead :
Address : Komp. Ruko Seroja Blok F No. 27
No. Telp : 0778 352 6147 / 0812 4539 1768
Email : kencanatirtamandiri@mailbox.example
Website : www.kencanatirtamandiri.example

Target Market(s)

Buyer Property Real Estate & Investor

Industry/Entity Type

Real Estate Development

Font styles to use
Serif
Sans Serif

Requirements
Must have
• according to your creative each other guys as long i need
• Address : Komp. Ruko Seroja Blok F No. 27
• No. Telp : 0778 352 6147 / 0812 4539 1768
• Email : kencanatirtamandiri@mailbox.example
• Website : www.kencanatirtamandiri.example
Nice to have
Should not have
• don't want another colour except : white , dark blue n gold suit to our logo developer real estate

```html
<!DOCTYPE html>
<html lang="en">
<head>
<meta charset="utf-8">
<title>Letterhead — PT. Kencana Tirta Mandiri Developer</title>
<link href="https://fonts.googleapis.com/css2?family=Open+Sans:wght@400;600;700&display=swap" rel="stylesheet">
<style>
  :root {
    --navy: #12365c;
    --gold: #c08632;
    --ink: #1b1b1b;
    --muted: #4a4a4a;
    --paper: #ffffff;
    --backdrop: #e9e9e9;
  }
  html, body {
    margin: 0;
    padding: 0;
    width: 1200px;
    height: 1105px;
    overflow: hidden;
    background: var(--backdrop);
    font-family: "Open Sans", Arial, sans-serif;
  }
  .letterhead {
    position: absolute;
    left: 225px;
    top: 22px;
    width: 750px;
    height: 1061px;
    background: var(--paper);
    box-shadow: 0 4px 18px rgba(0,0,0,0.12);
    color: var(--ink);
  }
  .brand {
    position: absolute;
    left: 70px;
    top: 90px;
    display: flex;
    align-items: center;
    gap: 12px;
  }
  .brand-dot {
    width: 16px;
    height: 16px;
    border-radius: 50%;
    background: var(--navy);
  }
  .brand-name {
    font-weight: 700;
    font-size: 20px;
    letter-spacing: 0.5px;
    color: var(--navy);
    line-height: 1.2;
  }
  .contact {
    position: absolute;
    right: 60px;
    top: 88px;
    padding-left: 22px;
    border-left: 1.5px solid var(--navy);
    font-size: 9.5px;
    line-height: 1.25;
    color: var(--muted);
  }
  .contact-row {
    display: flex;
    gap: 10px;
    align-items: flex-start;
    margin: 4px 0 6px;
  }
  .contact-row svg { width: 12px; height: 12px; flex: none; margin-top: 1px; }
  .contact strong { color: var(--ink); font-weight: 700; }
  .recipient {
    position: absolute;
    right: 80px;
    top: 215px;
    width: 150px;
    text-align: right;
    font-size: 13px;
    line-height: 1.4;
  }
  .letter-body {
    position: absolute;
    left: 90px;
    right: 90px;
    top: 300px;
    font-size: 13.2px;
    line-height: 1.45;
    text-align: justify;
  }
  .letter-body p { margin: 0 0 8px; }
  .signoff {
    margin-top: 24px;
    font-size: 12px;
  }
  .signoff .signer {
    display: block;
    font-weight: 700;
    font-size: 16px;
    margin-top: 4px;
  }
  .footer-band {
    position: absolute;
    left: 0;
    bottom: 0;
    width: 750px;
    height: 34px;
  }
</style>
</head>
<body>
  <main class="letterhead">
    <header>
      <div class="brand">
        <span class="brand-dot"></span>
        <span class="brand-name">PT. Kencana Tirta Mandiri Developer</span>
      </div>
      <address class="contact">
        <div class="contact-row">
          <svg viewBox="0 0 12 12"><path d="M2.5 1l2 2-1 1.3c.6 1.4 1.7 2.5 3.2 3.2l1.3-1 2 2-1.3 1.5C5 9.5 2.5 7 1 2.3z" fill="var(--navy)"/></svg>
          <span><strong>0812 4539 1768</strong><br>0778 352 6147</span>
        </div>
        <div class="contact-row">
          <svg viewBox="0 0 12 12"><path d="M6 0.8a3.6 3.6 0 0 0-3.6 3.6C2.4 7 6 11.2 6 11.2S9.6 7 9.6 4.4A3.6 3.6 0 0 0 6 .8z" fill="var(--navy)"/><circle cx="6" cy="4.4" r="1.3" fill="#fff"/></svg>
          <span><strong>Komp. Ruko Seroja</strong><br>Blok F No. 27</span>
        </div>
        <div class="contact-row">
          <svg viewBox="0 0 12 12"><circle cx="6" cy="6" r="5" fill="none" stroke="var(--navy)" stroke-width="1.4"/><path d="M1 6h10M6 1c-2.4 2.8-2.4 7.2 0 10M6 1c2.4 2.8 2.4 7.2 0 10" fill="none" stroke="var(--navy)" stroke-width="1"/></svg>
          <span><strong>www.kencanatirtamandiri.example</strong><br>kencanatirtamandiri@mailbox.example</span>
        </div>
      </address>
    </header>

    <p class="recipient">Lorem ipsum dolor sit amet, consectetuer adipiscing elit, sed</p>

    <section class="letter-body">
      <p>Lorem ipsum dolor sit amet, consectetuer adipiscing elit, sed diam nonummy nibh euismod tincidunt ut laoreet dolore magna aliquam erat volutpat. Ut wisi enim ad minim veniam, quis nostrud exerci tation ullamcorper suscipit lobortis nisl ut aliquip ex ea commodo consequat. Duis autem vel eum iriure dolor in hendrerit in vulputate velit esse molestie consequat, vel illum dolore eu feugiat nulla facilisis at vero eros et accumsan et iusto odio dignissim qui blandit praesent luptatum zzril delenit augue duis dolore te feugait nulla facilisi.</p>
      <p>Lorem ipsum dolor sit amet, cons ectetuer adipiscing elit, sed diam nonummy nibh euismod tincidunt ut laoreet dolore magna aliquam erat volutpat. Ut wisi enim ad minim veniam, quis nostrud exerci tation ullamcorper suscipit lobortis nisl ut aliquip ex ea commodo consequat. Lorem ipsum dolor sit amet, consectetuer adipiscing elit, sed diam nonummy</p>
      <p>nibh euismod tincidunt ut laoreet dolore magna aliquam erat volutpat. Ut wisi enim ad minim veniam, quis nostrud exerci tation ullamcorper suscipit lobortis nisl ut aliquip ex ea commodo consequat. Duis autem vel eum iriure dolor in hendrerit in vulputate velit esse molestie consequat, vel illum dolore eu feugiat nulla facilisis at vero eros et accumsan et iusto odio dignissim qui blandit praesent luptatum zzril delenit augue duis dolore te feugait nulla facilisi.</p>
      <p>Lorem ipsum dolor sit amet, cons ectetuer adipiscing elit, sed diam nonummy nibvh euismod tincidunt ut laoreet dolore magna aliquam erat volutpat. Ut wisi enim ad minim veniam, quis</p>
      <div class="signoff">Regarts<span class="signer">Daniel Hartono</span></div>
    </section>

    <svg class="footer-band" viewBox="0 0 750 34" preserveAspectRatio="none" aria-hidden="true">
      <polygon points="0,0 362,0 348,34 0,34" fill="var(--gold)"/>
      <polygon points="376,0 750,0 750,34 362,34" fill="var(--navy)"/>
    </svg>
  </main>
</body>
</html>
```